Letter and Envelope Design For Juniper Crest Realty

Please design a letter and an envelope incorporating our logo (See Attached). We are also launched a business card contest. Since we want them to match, please feel free to submit a design for both the business card and also the letter design and envelope.

Requirements
Must have
• The envelope, the letter and the business cards must match somehow connecting the designs. We want them to have something that holds them together besides the logo.

```html
<!DOCTYPE html>
<html lang="en">
<head>
<meta charset="utf-8">
<title>Juniper Crest Realty Letterhead</title>
<link href="https://fonts.googleapis.com/css2?family=Montserrat:wght@600;700&family=Questrial&display=swap" rel="stylesheet">
<style>
  :root {
    --navy: #172a74;
    --ink: #1b1b1b;
    --frame: #d6d6d6;
    --paper: #ffffff;
    --footer-text: #e8ebf5;
    --footer-rule: #8d97c2;
  }
  * { margin: 0; padding: 0; box-sizing: border-box; }
  html, body {
    width: 871px; height: 1200px; overflow: hidden; background: var(--paper);
  }
  .canvas { position: relative; width: 871px; height: 1200px; }
  .sheet {
    position: absolute; left: 30px; top: 30px; width: 811px; height: 1142px;
    border: 1px solid var(--frame); background: var(--paper);
  }
  .brand {
    position: absolute; left: 0; top: 40px; width: 811px; text-align: center;
  }
  .brand-mark { display: block; margin: 0 auto 8px; }
  .brand-name {
    font-family: "Montserrat", sans-serif; font-weight: 700; color: var(--navy);
    font-size: 17px; letter-spacing: 2.5px; line-height: 21px;
  }
  .text {
    font-family: "Questrial", sans-serif; color: var(--ink);
  }
  .recipient, .signature {
    position: absolute; left: 77px; font-size: 15px; line-height: 18px;
  }
  .recipient { top: 206px; }
  .strong { font-family: "Montserrat", sans-serif; font-weight: 700; font-size: 14.5px; }
  .company { margin-top: 18px; }
  .body {
    position: absolute; left: 77px; top: 383px; width: 662px;
    font-size: 12.4px; line-height: 19.2px;
  }
  .body p + p { margin-top: 19.2px; }
  .signature { top: 913px; }
  .footer {
    position: absolute; left: 0; bottom: 0; width: 809px; height: 118px;
    background: var(--navy); color: var(--footer-text); text-align: center;
    font-family: "Questrial", sans-serif;
  }
  .footer-address { padding-top: 23px; font-size: 11px; line-height: 15.5px; }
  .footer-rule {
    width: 358px; height: 1px; background: var(--footer-rule); margin: 10px auto 8px;
  }
  .footer-contacts { font-size: 10.5px; display: flex; justify-content: center; gap: 12px; }
  .footer-contacts span { display: inline-flex; align-items: center; gap: 3px; }
</style>
</head>
<body>
<div class="canvas">
  <div class="sheet">
    <header class="brand">
      <svg class="brand-mark" width="72" height="72" viewBox="0 0 72 72" aria-hidden="true">
        <circle cx="36" cy="36" r="33" fill="none" stroke="var(--navy)" stroke-width="3.5"/>
      </svg>
      <div class="brand-name">JUNIPER CREST<br>REALTY</div>
    </header>

    <section class="recipient text">
      <div class="strong">To:</div>
      <div class="strong">Daniel Moreno</div>
      <div>CEO</div>
      <div class="company strong">Harbor Line Group, Inc</div>
      <div>123 Street Name, Town City</div>
      <div>State, Country 556</div>
    </section>

    <section class="body text">
      <p>Lorem ipsum dolor sit amet, consectetur adipiscing elit. Ut et pharetra eros. Mauris quis pharetra ipsum. Proin eget imperdiet tellus, ac aliquam metus. Phasellus dignissim ex mi. Donec nisl tellus, malesuada et vestibulum vitae, feugiat a metus. Aliquam id convallis metus, ac pharetra ligula. Quisque sapien neque, hendrerit ac nisi sit amet, finibus porta nibh. Curabitur ante nibh, molestie quis convallis non, lacinia at ligula. Suspendisse commodo ullamcorper augue non dignissim. Proin convallis nunc vitae lectus egestas pretium. Nunc sed aliquam neque. Ut mauris arcu, porttitor in lectus sed, feugiat consequat odio. Nam laoreet risus suscipit neque dictum, non varius enim dignissim.</p>
      <p>Mauris sed ex pellentesque enim maximus lobortis. Nulla velit mauris, lacinia at egestas eu, fringilla at justo. Donec pharetra sagittis tincidunt. Proin maximus, velit at eleifend sagittis, nunc turpis sodales mauris, vitae ullamcorper lectus nulla in libero. Quisque nec placerat dolor. Mauris sit amet scelerisque orci. Praesent a viverra purus.</p>
      <p>Nunc aliquet nibh vitae accumsan dapibus. Fusce porttitor odio vel tortor laoreet faucibus. Nulla gravida turpis fringilla, hendrerit dui quis, imperdiet massa. Cras euismod egestas ante, nec rhoncus nisl dictum in. Nulla diam augue, pretium ut turpis volutpat, fermentum blandit metus. Vestibulum consequat ullamcorper felis eu cursus. Maecenas cursus, dui nec consectetur euismod, dolor justo pellentesque massa, non tempor neque ipsum in dolor. Praesent vestibulum gravida risus nec porta. Nunc non egestas sapien. Suspendisse dictum metus eu nulla dapibus, a semper enim efficitur. Etiam erat lorem, scelerisque sit amet nibh id, vehicula consequat odio. Pellentesque non sem lectus. Phasellus mattis magna tincidunt quam rutrum, vitae aliquam neque euismod.</p>
      <p>Praesent in mi a mi interdum tempus. Mauris pulvinar sit amet ante in consequat. Proin sit amet sem nulla. In nec est cursus, venenatis lectus sed, mollis eros. Vivamus blandit sagittis nisl. Cras malesuada vitae sem eu mollis. Morbi velit turpis, fermentum sit amet tempus at, consequat ac lacus. Donec tempus neque in egestas cursus.</p>
    </section>

    <section class="signature text">
      <div class="strong">Lena M. Whitford</div>
      <div>Office Manager</div>
    </section>

    <footer class="footer">
      <div class="footer-address">
        JUNIPER CREST REALTY, Inc.<br>
        4716 Alder Lane<br>
        Brookfield, NJ 07310
      </div>
      <div class="footer-rule"></div>
      <div class="footer-contacts">
        <span>
          <svg width="8" height="8" viewBox="0 0 8 8" aria-hidden="true"><circle cx="4" cy="4" r="3.4" fill="none" stroke="currentColor" stroke-width="0.9"/><path d="M2.6 2.4 Q2.8 4.8 5.6 5.4" fill="none" stroke="currentColor" stroke-width="0.9"/></svg>
          555-201-4387
        </span>
        <span>
          <svg width="8" height="8" viewBox="0 0 8 8" aria-hidden="true"><circle cx="4" cy="4" r="3.4" fill="none" stroke="currentColor" stroke-width="0.9"/><rect x="2.6" y="2.4" width="2.8" height="3.2" fill="none" stroke="currentColor" stroke-width="0.8"/></svg>
          555-201-7843
        </span>
        <span>
          <svg width="8" height="8" viewBox="0 0 8 8" aria-hidden="true"><circle cx="4" cy="4" r="3.4" fill="none" stroke="currentColor" stroke-width="0.9"/><circle cx="4" cy="4" r="1.6" fill="currentColor"/></svg>
          hello@junipercrest-realty.com
        </span>
      </div>
    </footer>
  </div>
</div>
</body>
</html>
```